Bref créative
VELMORA BUSINESS CARDS
VELMORA BC
Professional
Anselmo Tribaldes
Director General
Fidencio Lozano 4817. Local 5 Altos.
Colonia Almendros.
Nuevo Laredo, Tamaulipas 88172.
Mexico.
anselmo@velmora-ejemplo.com
www.velmora-ejemplo.com
* Importacion y Exportacion.
* Comercializacion y Procura.
* Transporte LTL, Van Trailers, Flatbed, Oversize cargo.
* Soluciones de logistica.
* Aduanas.
Vector Logo file

```html
<!DOCTYPE html>
<html lang="es">
<head>
<meta charset="utf-8">
<title>VELMORA BC – Tarjetas de presentación</title>
<link rel="stylesheet" href="https://fonts.googleapis.com/css2?family=Roboto:ital,wght@0,400;0,500;0,700;0,900;1,400&display=swap">
<style>
  :root {
    --bg: #e4e5e7;
    --navy: #2b2c8f;
    --navy-deep: #1f1f73;
    --navy-light: #3d43b5;
    --white: #ffffff;
    --ink: #151515;
    --muted: #8d8f95;
    --ring: #d7d8dc;
    --on-navy: #dfe2ff;
  }
  * { box-sizing: border-box; margin: 0; padding: 0; }
  html, body { width: 1200px; height: 799px; overflow: hidden; }
  body {
    background: var(--bg);
    font-family: "Roboto", Arial, sans-serif;
    position: relative;
  }
  .card {
    position: absolute;
    width: 540px;
    height: 309px;
    border-radius: 4px;
    overflow: hidden;
    box-shadow: 0 10px 28px rgba(0,0,0,.18);
  }

  /* Front */
  .card--front {
    left: 45px; top: 245px;
    background: linear-gradient(135deg, var(--navy-light) 0%, var(--navy) 45%, var(--navy-deep) 100%);
    color: var(--white);
  }
  .tagline {
    position: absolute; top: 26px; left: 0; right: 0;
    text-align: center; font-size: 10px; line-height: 1.45;
    color: var(--on-navy); font-style: italic;
  }
  .brand {
    display: flex; align-items: center; gap: 10px;
    font-weight: 900; letter-spacing: 2px;
  }
  .brand__dot { border-radius: 50%; }
  .card--front .brand {
    position: absolute; left: 0; right: 0; top: 118px;
    justify-content: center; font-size: 54px; color: var(--white);
  }
  .card--front .brand__dot { width: 18px; height: 18px; background: var(--white); }
  .website {
    position: absolute; right: 26px; bottom: 22px;
    font-size: 11px; color: var(--on-navy);
  }

  /* Back */
  .card--back {
    left: 615px; top: 245px;
    background: var(--white);
    color: var(--white);
  }
  .card--back svg.backdrop { position: absolute; inset: 0; }
  .person { position: absolute; left: 24px; top: 92px; }
  .person__name { font-size: 17px; font-weight: 700; }
  .person__role { font-size: 10px; color: var(--on-navy); margin-top: 2px; }
  .address {
    position: absolute; left: 24px; top: 148px;
    font-size: 10px; line-height: 1.45; color: var(--on-navy);
  }
  .contacts {
    position: absolute; left: 24px; top: 214px;
    list-style: none; font-size: 9.5px; color: var(--on-navy);
  }
  .contacts li { display: flex; align-items: center; gap: 7px; height: 15px; }
  .contacts svg { width: 10px; height: 10px; flex: none; }
  .card--back .brand {
    position: absolute; left: 322px; top: 126px;
    font-size: 36px; color: var(--ink);
  }
  .card--back .brand__dot { width: 12px; height: 12px; background: var(--navy); }
  .radio-id {
    position: absolute; left: 392px; top: 180px;
    display: flex; align-items: center; gap: 6px;
    font-size: 12px; font-weight: 700; color: var(--ink);
  }
  .radio-id svg { width: 14px; height: 14px; }
</style>
</head>
<body>

  <section class="card card--front" aria-label="Tarjeta frontal">
    <p class="tagline">
      Flete Marítimo para Centro y Sudamérica &nbsp;•&nbsp; Flete Aéreo &nbsp;•&nbsp; Entregas Urgentes<br>
      Nuestra especialidad cargas nacionales e internacionales con servicio de Puerta a Puerta
    </p>
    <div class="brand"><span>VELMORA</span><span class="brand__dot"></span></div>
    <p class="website">www.velmora-ejemplo.com</p>
  </section>

  <section class="card card--back" aria-label="Tarjeta de contacto">
    <svg class="backdrop" viewBox="0 0 540 309" preserveAspectRatio="none" aria-hidden="true">
      <defs>
        <linearGradient id="panel" x1="0" y1="0" x2="1" y2="1">
          <stop offset="0" stop-color="#3d43b5"/>
          <stop offset="1" stop-color="#1f1f73"/>
        </linearGradient>
      </defs>
      <circle cx="405" cy="160" r="150" fill="none" stroke="#d7d8dc" stroke-width="18"/>
      <path d="M0 0 H270 C215 70 300 170 300 309 H0 Z" fill="#5a62d0"/>
      <path d="M0 0 H250 C195 80 280 170 282 309 H0 Z" fill="url(#panel)"/>
    </svg>

    <div class="person">
      <h1 class="person__name">Anselmo Tribaldes</h1>
      <p class="person__role">Director General</p>
    </div>
    <address class="address" style="font-style:normal">
      Fidencio Lozano 4817. Local 5 Altos.<br>
      Colonia Almendros. Nuevo Laredo,<br>
      Tamaulipas 88172. Mexico.
    </address>
    <ul class="contacts">
      <li><svg viewBox="0 0 10 10"><circle cx="5" cy="5" r="5" fill="#dfe2ff"/><path d="M3 2.6l1 1-.5.7a4 4 0 0 0 2.2 2.2l.7-.5 1 1-.8.9C4.6 7.6 2.4 5.4 2.1 3.4z" fill="#2b2c8f"/></svg>867-555-0148</li>
      <li><svg viewBox="0 0 10 10"><circle cx="5" cy="5" r="5" fill="#dfe2ff"/><path d="M3 2.6l1 1-.5.7a4 4 0 0 0 2.2 2.2l.7-.5 1 1-.8.9C4.6 7.6 2.4 5.4 2.1 3.4z" fill="#2b2c8f"/></svg>867-555-0192</li>
      <li><svg viewBox="0 0 10 10"><circle cx="5" cy="5" r="5" fill="#dfe2ff"/><rect x="2.5" y="3.3" width="5" height="3.4" fill="none" stroke="#2b2c8f" stroke-width=".8"/><path d="M2.5 3.3L5 5.3l2.5-2" fill="none" stroke="#2b2c8f" stroke-width=".8"/></svg>anselmo@velmora-ejemplo.com</li>
      <li><svg viewBox="0 0 10 10"><circle cx="5" cy="5" r="5" fill="#dfe2ff"/><circle cx="5" cy="5" r="2.6" fill="none" stroke="#2b2c8f" stroke-width=".8"/><path d="M2.4 5h5.2M5 2.4v5.2" stroke="#2b2c8f" stroke-width=".6"/></svg>www.velmora-ejemplo.com</li>
    </ul>

    <div class="brand"><span>VELMORA</span><span class="brand__dot"></span></div>
    <p class="radio-id">
      <svg viewBox="0 0 14 14" aria-hidden="true"><rect x="4" y="1" width="6" height="12" rx="1.2" fill="#151515"/><rect x="5.2" y="2.6" width="3.6" height="3" fill="#fff"/></svg>
      52*164920*3
    </p>
  </section>

</body>
</html>
```